Cedarline Health Inc. Business Card and Stationery
Business Logo  - Health
Business Logo
Professional
Teresa Okonkwo
Registered Office: 14 S Pebblecroft Ln Schaumburg IL 60195 Phone: 847-555-0182 WareHouse Address: 2417 Bellhaven Street Schaumburg IL 60174 Phone: 847-555-0147
teresa@cedarlinehealth.example
www.cedarlinehealth.example

```html
<!DOCTYPE html>
<html lang="en">
<head>
<meta charset="utf-8">
<title>Cedarline Health Inc. Business Card and Stationery</title>
<link href="https://fonts.googleapis.com/css2?family=Open+Sans:wght@400;600;700&display=swap" rel="stylesheet">
<style>
  :root{
    --bg:#2b2b2d;
    --bg-stripe:#333336;
    --paper:#ffffff;
    --green:#6cb33f;
    --green-light:#a6d17a;
    --blue:#1d5ea8;
    --ink:#333333;
    --muted:#8a8a8a;
    --field:#d9d9d9;
    --caption:#9a9a9a;
    --globe:#e6eef6;
  }
  *{box-sizing:border-box;margin:0;padding:0}
  html,body{width:1200px;height:358px;overflow:hidden}
  body{
    position:relative;
    background:repeating-linear-gradient(90deg,var(--bg) 0 14px,var(--bg-stripe) 14px 16px);
    font-family:"Open Sans",Arial,sans-serif;color:var(--ink);
  }
  .piece{position:absolute;background:var(--paper);overflow:hidden;box-shadow:0 2px 6px rgba(0,0,0,.5)}
  .wave{position:absolute;left:0;bottom:0;width:100%;display:block}
  .brand{display:flex;align-items:center;gap:4px;position:absolute}
  .brand-dot{border-radius:50%;background:var(--blue);flex:none}
  .brand-name{color:var(--blue);font-weight:700;white-space:nowrap}
  .caption{position:absolute;color:var(--caption);font-size:6px;text-align:center}
  .watermark{position:absolute;border-radius:50%;background:radial-gradient(circle at 40% 35%,#fff,var(--globe) 70%,#d3e1ee);opacity:.9}

  .hero-brand{left:12px;top:62px}
  .hero-brand .brand-dot{width:26px;height:26px}
  .hero-brand .brand-name{color:#fff;font-size:12px}
  .hero-tag{position:absolute;left:44px;top:92px;color:#ccc;font-size:7px}

  .card{width:152px;height:90px}
  .card .brand{left:8px;top:12px}
  .card .brand-dot{width:14px;height:14px}
  .card .brand-name{font-size:8px}
  .card-person{position:absolute;left:8px;top:36px;font-size:6px;line-height:1.35}
  .card-person strong{display:block;color:var(--blue);font-size:7px}

  .letter{width:235px;height:317px;top:19px}
  .letter .brand{left:12px;top:12px}
  .letter .brand-dot{width:18px;height:18px}
  .letter .brand-name{font-size:9px}
  .letter .watermark{width:130px;height:130px;left:52px;top:100px}
  .letter-foot{position:absolute;left:10px;right:10px;bottom:6px;color:#fff;font-size:4.5px;text-align:center}

  .form{position:absolute;left:12px;top:40px;width:211px;border-collapse:collapse;font-size:5px}
  .form td{border:1px solid #bbb;height:10px;padding:0 3px}
  .form td.fill{background:var(--field);width:70px}

  .envelope{left:684px;top:89px;width:264px;height:120px}
  .envelope .brand{left:50%;top:14px;transform:translateX(-50%)}
  .envelope .brand-dot{width:14px;height:14px}
  .envelope .brand-name{font-size:8px}
  .env-flap{position:absolute;inset:0}

  .slip{left:684px;top:224px;width:264px;height:106px}
  .slip .brand{top:44px}
  .slip .brand-dot{width:16px;height:16px}
  .slip .brand-name{font-size:8px}

  .rcard{left:967px;width:214px}
  .rcard .brand{left:10px;top:10px}
  .rcard .brand-dot{width:14px;height:14px}
  .rcard .brand-name{font-size:8px}
  .rcard-text{position:absolute;right:10px;top:10px;font-size:5.5px;text-align:right;line-height:1.4;color:var(--blue)}
</style>
</head>
<body>

  <div class="brand hero-brand"><span class="brand-dot"></span><span class="brand-name">Cedarline Health Inc.</span></div>
  <p class="hero-tag">Healthcare Company</p>

  <div class="piece card" style="left:12px;top:144px">
    <div class="brand"><span class="brand-dot"></span><span class="brand-name">Cedarline Health Inc.</span></div>
    <p class="card-person"><strong>Teresa Okonkwo</strong>Director</p>
    <svg class="wave" viewBox="0 0 152 30" height="30" preserveAspectRatio="none"><path d="M0 14 C40 4 90 24 152 8 V30 H0Z" fill="var(--green)"/><path d="M0 12 C40 2 90 22 152 6" stroke="var(--blue)" stroke-width="1.5" fill="none"/></svg>
  </div>
  <p class="caption" style="left:12px;top:237px;width:152px">Business Card Front</p>

  <div class="piece card" style="left:12px;top:247px;height:84px">
    <div class="brand"><span class="brand-dot"></span><span class="brand-name">Cedarline Health Inc.</span></div>
    <p class="card-person" style="top:32px"><strong>Teresa Okonkwo</strong>847-555-0182<br>teresa@cedarlinehealth.example<br>www.cedarlinehealth.example</p>
    <svg class="wave" viewBox="0 0 152 18" height="18" preserveAspectRatio="none"><path d="M0 10 C50 0 100 16 152 6 V18 H0Z" fill="var(--green)"/></svg>
  </div>
  <p class="caption" style="left:12px;top:333px;width:152px">Business Card Back</p>

  <div class="piece letter" style="left:173px">
    <div class="brand"><span class="brand-dot"></span><span class="brand-name">Cedarline Health Inc.</span></div>
    <div class="watermark" role="img" aria-label="Faint circular emblem"></div>
    <svg class="wave" viewBox="0 0 235 40" height="40" preserveAspectRatio="none"><path d="M0 10 C70 30 150 -4 235 16 V40 H0Z" fill="var(--green)"/><path d="M0 8 C70 28 150 -6 235 14" stroke="var(--blue)" stroke-width="2" fill="none"/></svg>
    <p class="letter-foot">14 S Pebblecroft Ln Schaumburg IL 60195 · 847-555-0182 · www.cedarlinehealth.example</p>
  </div>
  <p class="caption" style="left:173px;top:339px;width:235px">Letterhead</p>

  <div class="piece letter" style="left:425px">
    <div class="brand"><span class="brand-dot"></span><span class="brand-name">Cedarline Health Inc.</span></div>
    <table class="form">
      <tr><td>Date</td><td class="fill"></td><td>Ref</td><td class="fill"></td></tr>
      <tr><td>Name</td><td class="fill"></td><td>Phone</td><td class="fill"></td></tr>
      <tr><td>Item</td><td class="fill"></td><td>Qty</td><td class="fill"></td></tr>
      <tr><td>Signature</td><td class="fill" colspan="3"></td></tr>
    </table>
    <div class="watermark" role="img" aria-label="Faint circular emblem" style="top:120px"></div>
    <svg class="wave" viewBox="0 0 235 40" height="40" preserveAspectRatio="none"><path d="M0 10 C70 30 150 -4 235 16 V40 H0Z" fill="var(--green)"/><path d="M0 8 C70 28 150 -6 235 14" stroke="var(--blue)" stroke-width="2" fill="none"/></svg>
    <p class="letter-foot">2417 Bellhaven Street Schaumburg IL 60174 · 847-555-0147</p>
  </div>
  <p class="caption" style="left:425px;top:339px;width:235px">Order Form</p>

  <div class="piece envelope">
    <svg class="env-flap" viewBox="0 0 264 120" preserveAspectRatio="none"><path d="M0 0 L132 62 L264 0" stroke="#e2e2e2" fill="none"/></svg>
    <div class="brand"><span class="brand-dot"></span><span class="brand-name">Cedarline Health Inc.</span></div>
  </div>
  <p class="caption" style="left:684px;top:212px;width:264px">Envelope</p>

  <div class="piece slip">
    <svg style="position:absolute;left:0;top:0" width="60" height="106" viewBox="0 0 60 106"><path d="M0 0 H14 C34 30 6 70 26 106 H0Z" fill="var(--green)"/><path d="M14 0 C34 30 6 70 26 106" stroke="var(--blue)" stroke-width="2" fill="none"/></svg>
    <div class="brand" style="left:40px"><span class="brand-dot"></span><span class="brand-name">Cedarline Health Inc.</span></div>
  </div>
  <p class="caption" style="left:684px;top:338px;width:264px">Compliment Slip</p>

  <div class="piece rcard" style="top:101px;height:86px">
    <div class="brand"><span class="brand-dot"></span><span class="brand-name">Cedarline Health Inc.</span></div>
    <p class="rcard-text">Teresa Okonkwo<br>teresa@cedarlinehealth.example</p>
    <svg class="wave" viewBox="0 0 214 40" height="40" preserveAspectRatio="none"><path d="M0 18 C60 0 140 30 214 8 V40 H0Z" fill="var(--green)"/><path d="M0 24 C60 8 140 34 214 16 V40 H0Z" fill="var(--green-light)" opacity=".5"/></svg>
  </div>
  <p class="caption" style="left:967px;top:189px;width:214px">Business Card</p>

  <div class="piece rcard" style="top:211px;height:96px">
    <div class="brand"><span class="brand-dot"></span><span class="brand-name">Cedarline Health Inc.</span></div>
    <p class="rcard-text">847-555-0182<br>www.cedarlinehealth.example</p>
    <svg class="wave" viewBox="0 0 214 60" height="60" preserveAspectRatio="none"><path d="M0 20 C60 0 140 34 214 10 V60 H0Z" fill="var(--green)"/></svg>
  </div>
  <p class="caption" style="left:967px;top:309px;width:214px">Card Reverse</p>

</body>
</html>
```